KORVELTA Corporate Business Card

Modern business card design for company which focuses in the areas of Staffing, IT Consulting & Data Services. Please note: We are no longer using the IT subscript on the logo. All designs should have IT subscript removed.
Website: www.korveltait.example

```html
<!DOCTYPE html>
<html lang="en">
<head>
<meta charset="utf-8">
<title>KORVELTA Business Card</title>
<link href="https://fonts.googleapis.com/css2?family=Open+Sans:wght@400;700&family=Oswald:wght@500&display=swap" rel="stylesheet">
<style>
  :root {
    --backdrop: #3a3a3a;
    --card: #2a2a2a;
    --card-edge: #1f1f1f;
    --ink-light: #e6e6e6;
    --ink-soft: #c9c9c9;
    --accent: #1f9ad6;
    --divider: #8a8a8a;
  }
  * { margin: 0; padding: 0; box-sizing: border-box; }
  html, body {
    width: 1200px; height: 901px; overflow: hidden;
    background: var(--backdrop);
  }
  .canvas {
    position: relative; width: 1200px; height: 901px;
    display: flex; flex-direction: column; align-items: center; justify-content: center; gap: 40px;
  }
  .card {
    position: relative; width: 630px; height: 360px;
    background: var(--card);
    border: 1px solid var(--card-edge);
    box-shadow: 0 10px 28px rgba(0,0,0,0.45);
  }
  .card-front { display: flex; align-items: center; justify-content: center; }
  .brand {
    display: flex; align-items: center; gap: 14px;
  }
  .brand-mark {
    width: 30px; height: 30px; background: var(--ink-soft);
  }
  .brand-name {
    font-family: "Open Sans", sans-serif; font-weight: 700;
    font-size: 64px; letter-spacing: 4px; color: var(--ink-soft);
  }
  .card-back { font-family: "Open Sans", sans-serif; }
  .identity {
    position: absolute; left: 0; top: 150px; width: 278px; text-align: right;
  }
  .person-name {
    font-family: "Oswald", sans-serif; font-weight: 500;
    font-size: 34px; line-height: 1; color: var(--accent);
    letter-spacing: 0.5px; text-transform: uppercase;
  }
  .person-role {
    font-size: 17px; color: var(--ink-light); margin-top: 4px;
  }
  .divider {
    position: absolute; left: 298px; top: 140px; width: 1px; height: 82px;
    background: var(--divider);
  }
  .contact-list {
    position: absolute; left: 318px; top: 146px; list-style: none;
  }
  .contact-list li {
    display: flex; align-items: center; gap: 10px;
    font-size: 17px; line-height: 24px; color: var(--ink-light);
  }
  .contact-list svg { width: 14px; height: 14px; fill: var(--accent); flex: none; }
  .address {
    position: absolute; left: 0; right: 0; bottom: 56px; text-align: center;
    font-size: 18px; color: var(--ink-light);
  }
</style>
</head>
<body>
<main class="canvas">
  <section class="card card-front">
    <div class="brand">
      <span class="brand-mark"></span>
      <span class="brand-name">KORVELTA</span>
    </div>
  </section>

  <section class="card card-back">
    <div class="identity">
      <p class="person-name">Marcus Delaney</p>
      <p class="person-role">Manager</p>
    </div>
    <span class="divider"></span>
    <ul class="contact-list">
      <li>
        <svg viewBox="0 0 24 24" aria-hidden="true"><path d="M6.6 10.8a15.2 15.2 0 0 0 6.6 6.6l2.2-2.2a1 1 0 0 1 1-.25 11.4 11.4 0 0 0 3.6.57 1 1 0 0 1 1 1V20a1 1 0 0 1-1 1A17 17 0 0 1 3 4a1 1 0 0 1 1-1h3.5a1 1 0 0 1 1 1c0 1.25.2 2.45.57 3.57a1 1 0 0 1-.25 1z"/></svg>
        555-014-7290
      </li>
      <li>
        <svg viewBox="0 0 24 24" aria-hidden="true"><path d="M2 5h20v14H2z M2 5l10 8 10-8" /><path d="M2 6.5l10 7.5 10-7.5V19H2z" fill="#2a2a2a" opacity="0"/></svg>
        contactus@korveltait.example
      </li>
      <li>
        <svg viewBox="0 0 24 24" aria-hidden="true"><circle cx="12" cy="12" r="10"/><path d="M2 12h20M12 2c3 3 3 17 0 20M12 2c-3 3-3 17 0 20" stroke="#2a2a2a" stroke-width="1.6" fill="none"/></svg>
        www.korveltait.example
      </li>
    </ul>
    <p class="address">48 Harlow Ave., Brantfield, IN 40012</p>
  </section>
</main>
</body>
</html>
```